We are a music company that specializes in Music Mixing and Mastering. We also do vocal recording and create instrumentals for various artists. Our website is 731kv.com

Target Market(s)

Musicians, Record labels, rappers, and singers

Industry/Entity Type

Artists

Contact Information for Business Card

731KV
Industry Standard Mixing & Mastering
(484) 317-2095
sales@731kv.com
731kv.com

Requirements
Must have
• contact info and twitter (@731KV)

```html
<!DOCTYPE html>
<html lang="en">
<head>
<meta charset="utf-8">
<title>731KV Business Card</title>
<link rel="stylesheet" href="https://fonts.googleapis.com/css2?family=Quicksand:wght@500;700&display=swap">
<style>
  :root {
    --stage: #d6d6d6;
    --red: #d8232a;
    --red-deep: #b5161c;
    --white: #ffffff;
    --paper: #f4f4f4;
    --ink-black: #111111;
    --card-w: 630px;
    --card-h: 360px;
  }
  * { box-sizing: border-box; margin: 0; padding: 0; }
  html, body {
    width: 1200px;
    height: 900px;
    overflow: hidden;
    background: var(--stage);
    font-family: "Quicksand", sans-serif;
  }
  .sheet {
    width: 1200px;
    height: 900px;
    display: flex;
    flex-direction: column;
    align-items: center;
    justify-content: center;
    gap: 40px;
  }
  .card {
    position: relative;
    width: var(--card-w);
    height: var(--card-h);
    overflow: hidden;
    box-shadow: 0 6px 18px rgba(0,0,0,0.25);
  }

  /* Front */
  .card--front {
    background: radial-gradient(ellipse at 50% 40%, var(--white) 0%, var(--paper) 70%, #e6e6e6 100%);
  }
  .card--front .wordmark {
    position: absolute;
    top: 28px;
    left: 0;
    width: 100%;
    text-align: center;
    font-weight: 700;
    font-size: 140px;
    line-height: 1;
    letter-spacing: -2px;
    color: var(--red);
  }
  .card--front .tagline {
    position: absolute;
    top: 196px;
    left: 0;
    width: 100%;
    text-align: center;
    font-weight: 500;
    font-size: 29px;
    color: var(--red);
  }
  .contact-band {
    position: absolute;
    left: 0;
    bottom: 0;
    width: 100%;
    height: 88px;
    background: linear-gradient(180deg, var(--red) 0%, var(--red-deep) 100%);
    border-top: 4px solid var(--white);
    box-shadow: 0 -3px 0 var(--red);
    display: flex;
    align-items: center;
    justify-content: center;
    gap: 12px;
    color: var(--white);
    font-size: 17px;
    font-weight: 500;
  }
  .contact-band .label { font-weight: 700; }
  .contact-band .divider {
    width: 2px;
    height: 26px;
    background: linear-gradient(180deg, var(--white) 0 45%, transparent 45% 55%, var(--white) 55% 100%);
  }

  /* Back */
  .card--back {
    background: var(--ink-black);
  }
  .card--back .wordmark {
    position: absolute;
    top: 50px;
    left: 0;
    width: 100%;
    text-align: center;
    font-weight: 700;
    font-size: 150px;
    line-height: 1;
    letter-spacing: -2px;
    color: var(--red);
  }
  .card--back .tagline {
    position: absolute;
    top: 226px;
    left: 0;
    width: 100%;
    text-align: center;
    font-weight: 500;
    font-size: 29px;
    color: var(--red);
  }
  .social-handle {
    position: absolute;
    left: 26px;
    bottom: 24px;
    display: flex;
    align-items: center;
    gap: 10px;
    color: var(--white);
    font-weight: 700;
    font-size: 18px;
  }
  .social-handle .marker {
    width: 22px;
    height: 22px;
    background: var(--red);
    border-radius: 3px;
  }
</style>
</head>
<body>
  <main class="sheet">
    <section class="card card--front" aria-label="Business card front">
      <div class="wordmark">731KV</div>
      <p class="tagline">Industry Standard Mixing &amp; Mastering</p>
      <div class="contact-band">
        <span><span class="label">Phone:</span> (484) 317-2095</span>
        <span class="divider"></span>
        <span><span class="label">Email:</span> sales@731kv.com</span>
        <span class="divider"></span>
        <span><span class="label">Web:</span> www.731kv.com</span>
      </div>
    </section>

    <section class="card card--back" aria-label="Business card back">
      <div class="wordmark">731KV</div>
      <p class="tagline">Industry Standard Mixing &amp; Mastering</p>
      <div class="social-handle">
        <span class="marker"></span>
        <span>@731KV</span>
      </div>
    </section>
  </main>
</body>
</html>
```